Business Card Design

We need a business card design for our new expansion based in Bloomfield Hills, Michigan. Our company is Quiet Harbor Institute & Wellness Center. Our Academy teaches individuals of all ages and professions to live from their soul. We teach intuitive development, meditation and mindfulness; shamanic healing. And ourr healing center provides holistic services. We offer certification programs that support the ethical practices of Intuitive professionals. Our team of Intuitive Practitioners includes: doctors, psychologists, chiropractor, soul retrievers, mediums, etc who all balance their knowledge with intuitive wisdom.

We want our symbol to be the Blue Morpho Buttefly and the colors on the card to complement it. We want to communicate inspiration, healing and empowerment. Thank you
Updates

Industry/Entity Type

Business

Contact Information for Business Card

Dana Orwick
Medium. Author. Soul Retriever.
Founder, Quiet Harbor

Quiet Harbor

19 North Cedar Mill Drive Suite 100
Fernwood Heights, MI 48517
248-603-7418

www.danaorwick.example

Requirements
Must have
• blue morpho butterfly

```html
<!DOCTYPE html>
<html lang="en">
<head>
<meta charset="utf-8">
<title>Quiet Harbor – Business Card</title>
<link href="https://fonts.googleapis.com/css2?family=Saira:wght@400;500;600&display=swap" rel="stylesheet">
<style>
  :root {
    --backdrop: #e4e5e8;
    --card: #2f2f31;
    --text: #f2f2f2;
    --muted: #cfcfd2;
    --divider: #5a5a5e;
    --accent: #1a9ad9;
    --accent-deep: #4c58d0;
    --brand: #3f7fd6;
  }
  * { margin: 0; padding: 0; box-sizing: border-box; }
  html, body {
    width: 1200px; height: 817px; overflow: hidden;
    background: var(--backdrop);
    font-family: "Saira", sans-serif;
  }
  .canvas {
    width: 1200px; height: 817px;
    display: flex; align-items: center; justify-content: center;
  }
  .card {
    position: relative;
    width: 1000px; height: 571px;
    background: var(--card);
    border-radius: 30px;
    overflow: hidden;
    color: var(--text);
    box-shadow: 0 10px 30px rgba(0,0,0,.25);
  }
  .brand {
    position: absolute; top: 60px; right: 80px;
    display: flex; flex-direction: column; align-items: center; gap: 22px;
  }
  .brand-mark {
    width: 64px; height: 64px; border-radius: 50%;
    background: var(--brand);
  }
  .brand-name {
    font-size: 38px; font-weight: 500;
    letter-spacing: 4px; text-transform: uppercase;
    color: var(--brand);
  }
  .identity {
    position: absolute; top: 250px; left: 70px;
    display: flex; align-items: center; gap: 14px;
  }
  .identity svg { width: 36px; height: 40px; }
  .person-name {
    font-size: 31px; font-weight: 500; letter-spacing: 1px;
    text-transform: uppercase;
  }
  .sep { font-size: 30px; margin: 0 6px; }
  .role {
    font-size: 19px; letter-spacing: 1px; text-transform: uppercase;
    color: var(--muted);
  }
  .contacts {
    position: absolute; top: 320px; left: 40px; right: 40px;
    display: flex;
  }
  .contact {
    flex: 1;
    display: flex; flex-direction: column; align-items: center; gap: 22px;
    padding: 6px 18px 4px;
    min-width: 0;
  }
  .contact + .contact { border-left: 2px solid var(--divider); }
  .icon-badge {
    width: 64px; height: 64px; border-radius: 50%;
    background: var(--accent);
    display: flex; align-items: center; justify-content: center;
  }
  .icon-badge svg { width: 34px; height: 34px; }
  .contact-text { font-size: 22px; letter-spacing: 0.5px; white-space: nowrap; }
  .address-band {
    position: absolute; left: 0; right: 0; bottom: 28px; height: 52px;
    background: linear-gradient(90deg, var(--accent-deep), var(--accent) 55%, var(--accent-deep));
    display: flex; align-items: center; gap: 14px;
    padding-left: 48px;
    font-size: 20px; letter-spacing: 1px;
  }
  .address-band svg { width: 20px; height: 26px; }
</style>
</head>
<body>
<main class="canvas">
  <section class="card">
    <div class="brand">
      <span class="brand-mark"></span>
      <span class="brand-name">Quiet Harbor</span>
    </div>

    <div class="identity">
      <svg viewBox="0 0 36 40" aria-hidden="true">
        <circle cx="18" cy="11" r="9" fill="#dcdcdc"/>
        <path d="M2 40 C2 28 9 22 18 22 C27 22 34 28 34 40 Z" fill="#dcdcdc"/>
      </svg>
      <span class="person-name">Dana Orwick</span>
      <span class="sep">|</span>
      <span class="role">Founder</span>
    </div>

    <div class="contacts">
      <div class="contact">
        <span class="icon-badge">
          <svg viewBox="0 0 34 34" aria-hidden="true">
            <rect x="10" y="3" width="14" height="28" rx="2.5" fill="none" stroke="#fff" stroke-width="2.4"/>
            <line x1="10" y1="8" x2="24" y2="8" stroke="#fff" stroke-width="2"/>
            <line x1="10" y1="25" x2="24" y2="25" stroke="#fff" stroke-width="2"/>
            <circle cx="17" cy="28" r="1.3" fill="#fff"/>
          </svg>
        </span>
        <span class="contact-text">248-603-7418</span>
      </div>
      <div class="contact">
        <span class="icon-badge">
          <svg viewBox="0 0 34 34" aria-hidden="true">
            <rect x="4" y="8" width="26" height="18" rx="1.5" fill="#fff"/>
            <path d="M4 9 L17 19 L30 9" fill="none" stroke="#1a9ad9" stroke-width="2"/>
          </svg>
        </span>
        <span class="contact-text">hello@danaorwick.example</span>
      </div>
      <div class="contact">
        <span class="icon-badge">
          <svg viewBox="0 0 34 34" aria-hidden="true" fill="none" stroke="#fff" stroke-width="2">
            <circle cx="17" cy="17" r="13"/>
            <ellipse cx="17" cy="17" rx="6" ry="13"/>
            <line x1="4" y1="17" x2="30" y2="17"/>
            <path d="M6 10 H28 M6 24 H28"/>
          </svg>
        </span>
        <span class="contact-text">www.danaorwick.example</span>
      </div>
    </div>

    <div class="address-band">
      <svg viewBox="0 0 20 26" aria-hidden="true">
        <path d="M10 1 C4.5 1 1 5 1 10 C1 17 10 25 10 25 C10 25 19 17 19 10 C19 5 15.5 1 10 1 Z" fill="#fff"/>
        <circle cx="10" cy="10" r="3.5" fill="#3f6fd4"/>
      </svg>
      <span class="address-text">19 North Cedar Mill Drive Suite 100, Fernwood Heights, MI 48517</span>
    </div>
  </section>
</main>
</body>
</html>
```